Presentation Flyer for Married Couple at night separate business owners by day

I would like a flyer to use to advertise free presentations put on by husband and I. I (Renata Volkhaven) am an estate planning attorney that works for PWR Law. My husband (Dan Volkhaven) is a financial planner that works for Quelmora Financial Planning. Would love it to be funny but serious. At night we are a married couple of 4 children, by day we individually work with people helping them protect their assets and their families.
Goal is for this to be used for multiple events.
Things to include: Food will be provided, Raffle for $500 off an Estate Plan Package
Topics to be covered in Seminar:
Estate & Financial Planning Essentials

Protect Your Future
Build a strong financial foundation with emergency funds, retirement planning, and smart investment strategies that match your goals.

Secure Your Legacy
Learn about wills, trusts, and powers of attorney - the essential documents everyone needs to protect their family's future.

Guard Your Assets
Understand the right insurance coverage to protect yourself and your loved ones, from life insurance to long-term care options.

Transfer Wealth Wisely
Discover tax-efficient strategies for passing assets to the next generation and making the most of your charitable giving.

```html
<!DOCTYPE html>
<html lang="en">
<head>
<meta charset="utf-8">
<title>Estate &amp; Financial Planning Essentials Seminar</title>
<link href="https://fonts.googleapis.com/css2?family=Poppins:wght@400;500;600;700&display=swap" rel="stylesheet">
<style>
  :root {
    --teal-deep: #1d5a54;
    --teal: #17706e;
    --blue: #14508a;
    --navy: #173a63;
    --bright-blue: #1d5ea8;
    --gold: #f2cf8f;
    --panel: #f2f3f6;
    --white: #ffffff;
  }
  * { margin: 0; padding: 0; box-sizing: border-box; }
  html, body { width: 928px; height: 1200px; overflow: hidden; background: var(--white); }
  body { font-family: 'Poppins', sans-serif; }
  .flyer { position: relative; width: 928px; height: 1200px; overflow: hidden; }

  .hero { position: absolute; left: 0; top: 0; width: 928px; height: 362px; }
  .hero-art { position: absolute; inset: 0; }
  .hero-text { position: absolute; left: 52px; top: 62px; color: var(--white); }
  .hero-title { font-size: 35px; font-weight: 500; line-height: 43px; letter-spacing: 0.3px; }
  .hero-seminar { font-size: 60px; font-weight: 700; color: var(--gold); line-height: 72px; margin-top: 6px; }
  .hero-tagline { font-size: 27px; font-weight: 400; line-height: 33px; margin-top: 18px; }

  .topics { position: absolute; left: 0; top: 362px; width: 928px; height: 232px; background: var(--blue); }
  .topic { position: absolute; width: 410px; height: 70px; color: var(--white); }
  .topic-icon { position: absolute; left: 0; top: 0; width: 68px; height: 68px; border: 1.5px solid var(--white); border-radius: 7px; }
  .topic-icon svg { width: 100%; height: 100%; }
  .topic-title { position: absolute; left: 81px; top: -4px; font-size: 21px; font-weight: 500; white-space: nowrap; }
  .topic-body { position: absolute; left: 81px; top: 28px; width: 325px; font-size: 11.3px; line-height: 14.5px; }
  .topic-body.justified { text-align: justify; }

  .portrait { position: absolute; left: 0; top: 594px; width: 465px; height: 529px;
    background: linear-gradient(120deg, #b07a5c 0%, #8f5a43 35%, #2a3550 60%, #1e2840 100%); }

  .contacts { position: absolute; left: 465px; top: 594px; width: 463px; height: 529px; background: var(--panel); }
  .firm-mark { position: absolute; background: var(--white); display: flex; align-items: center; justify-content: center; gap: 10px; }
  .firm-mark .name { font-size: 22px; font-weight: 600; }
  .firm-mark .dot { width: 12px; height: 12px; }
  .firm-law { left: 104px; top: 43px; width: 245px; height: 92px; }
  .firm-law .name { color: var(--navy); }
  .firm-law .dot { background: var(--navy); }
  .firm-finance { left: 148px; top: 272px; width: 157px; height: 100px; flex-direction: column; gap: 6px; }
  .firm-finance .name { color: var(--teal); font-size: 15px; text-align: center; line-height: 19px; }
  .firm-finance .dot { background: var(--teal); border-radius: 50%; }

  .person-name { position: absolute; left: 0; width: 463px; text-align: center; font-size: 30px; font-weight: 500; color: var(--navy); }
  .person-role { position: absolute; left: 0; width: 463px; text-align: center; font-size: 16px; font-weight: 500; letter-spacing: 0.3px; }
  .attorney .first { color: var(--bright-blue); }
  .planner .first { color: var(--teal); }
  .attorney.person-role { color: var(--blue); }
  .planner.person-role { color: var(--teal); }

  .contact-pill { position: absolute; left: 47px; width: 360px; height: 25px; border-radius: 7px; color: var(--white);
    font-size: 13px; display: flex; align-items: center; justify-content: center; gap: 16px; white-space: nowrap; }
  .contact-pill span { display: inline-flex; align-items: center; gap: 3px; }
  .contact-pill svg { width: 10px; height: 10px; fill: var(--white); }
  .pill-attorney { top: 213px; background: var(--blue); }
  .pill-planner { top: 458px; background: var(--teal); gap: 6px; }

  .footer { position: absolute; top: 1123px; height: 77px; color: var(--white); font-size: 13px; font-weight: 500;
    text-align: center; line-height: 17px; display: flex; flex-direction: column; justify-content: center; letter-spacing: 0.2px; }
  .footer-couple { left: 0; width: 465px; background: var(--teal); }
  .footer-event { left: 465px; width: 463px; background: var(--blue); }
</style>
</head>
<body>
<main class="flyer">

  <header class="hero">
    <svg class="hero-art" viewBox="0 0 928 362" preserveAspectRatio="none">
      <defs>
        <linearGradient id="houseTone" x1="0" y1="0" x2="1" y2="1">
          <stop offset="0" stop-color="#1f5f55"/>
          <stop offset="0.6" stop-color="#2a6a58"/>
          <stop offset="1" stop-color="#3a7560"/>
        </linearGradient>
        <linearGradient id="familyTone" x1="0" y1="0" x2="1" y2="1">
          <stop offset="0" stop-color="#c9a98a"/>
          <stop offset="0.45" stop-color="#d9b594"/>
          <stop offset="1" stop-color="#e9e4dc"/>
        </linearGradient>
      </defs>
      <rect width="928" height="362" fill="url(#houseTone)" role="img" aria-label="Photo of a brick family home behind trees, tinted green"/>
      <polygon points="458,0 928,0 928,362 555,362 600,200" fill="url(#familyTone)" role="img" aria-label="Photo of a smiling family of four sitting close together"/>
      <polygon points="775,0 928,0 928,140" fill="#1f6a62" opacity="0.85"/>
    </svg>
    <div class="hero-text">
      <h1 class="hero-title">Estate &amp; Financial<br>Planning Essentials</h1>
      <div class="hero-seminar">Seminar:</div>
      <p class="hero-tagline">Helping people protect<br>their assets &amp; their families</p>
    </div>
  </header>

  <section class="topics">
    <article class="topic" style="left:54px; top:22px;">
      <div class="topic-icon">
        <svg viewBox="0 0 68 68" fill="none" stroke="#fff" stroke-width="1.6" stroke-linecap="round">
          <circle cx="34" cy="24" r="11"/>
          <text x="34" y="29.5" text-anchor="middle" font-size="15" font-family="Poppins, sans-serif" fill="#fff" stroke="none">$</text>
          <path d="M34 35v21M34 48c-3-5-9-6-13-4 3 5 9 6 13 4zM34 48c3-5 9-6 13-4-3 5-9 6-13 4z"/>
        </svg>
      </div>
      <h2 class="topic-title">Protect Your Future</h2>
      <p class="topic-body">Build a strong financial foundation with emergency funds, retirement planning, and smart investment strategies that match your goals.</p>
    </article>

    <article class="topic" style="left:474px; top:22px;">
      <div class="topic-icon">
        <svg viewBox="0 0 68 68" fill="none" stroke="#fff" stroke-width="1.6" stroke-linecap="round" stroke-linejoin="round">
          <path d="M20 50V20h26v8M20 50c0 3 3 4 5 4h19c2 0 3-2 3-4v-4H25v4c0 2-2 4-5 4"/>
          <path d="M26 28h12M26 34h10M26 40h8"/>
          <path d="M40 44c2-9 8-16 14-18-1 7-6 14-14 18zM40 44l7-9"/>
        </svg>
      </div>
      <h2 class="topic-title">Secure Your Legacy</h2>
      <p class="topic-body justified">Learn about wills, trusts, and powers of attorney - the essential documents everyone needs to protect their family's future.</p>
    </article>

    <article class="topic" style="left:54px; top:132px;">
      <div class="topic-icon">
        <svg viewBox="0 0 68 68" fill="none" stroke="#fff" stroke-width="1.6" stroke-linejoin="round">
          <path d="M34 15l16 5v14c0 10-7 16-16 20-9-4-16-10-16-20V20z"/>
          <text x="34" y="41" text-anchor="middle" font-size="20" font-weight="600" font-family="Poppins, sans-serif" fill="#fff" stroke="none">$</text>
        </svg>
      </div>
      <h2 class="topic-title">Guard Your Assets</h2>
      <p class="topic-body">Understand the right insurance coverage to protect yourself and your loved ones, from life insurance to long-term care options.</p>
    </article>

    <article class="topic" style="left:474px; top:132px;">
      <div class="topic-icon">
        <svg viewBox="0 0 68 68" fill="none" stroke="#fff" stroke-width="1.6" stroke-linecap="round" stroke-linejoin="round">
          <path d="M22 24a14 14 0 0 1 25 4M46 44a14 14 0 0 1-25-4"/>
          <path d="M22 19v5h5M46 49v-5h-5"/>
          <text x="34" y="42" text-anchor="middle" font-size="19" font-weight="600" font-family="Poppins, sans-serif" fill="#fff" stroke="none">$</text>
        </svg>
      </div>
      <h2 class="topic-title">Transfer Wealth Wisely</h2>
      <p class="topic-body justified">Discover tax-efficient strategies for passing assets to the next generation and making the most of your charitable giving.</p>
    </article>
  </section>

  <div class="portrait" role="img" aria-label="Photo of the couple, Renata and Dan Volkhaven, seated together in front of a brick wall"></div>

  <section class="contacts">
    <div class="firm-mark firm-law"><span class="dot"></span><span class="name">PWR Law</span></div>
    <h3 class="person-name attorney" style="top:133px;"><span class="first">Renata</span> Volkhaven</h3>
    <p class="person-role attorney" style="top:180px;">ESTATE PLANNING ATTORNEY</p>
    <div class="contact-pill pill-attorney">
      <span><svg viewBox="0 0 24 24"><path d="M6.6 10.8a15 15 0 0 0 6.6 6.6l2.2-2.2c.3-.3.7-.4 1-.2 1.1.4 2.3.6 3.6.6.6 0 1 .4 1 1V20c0 .6-.4 1-1 1A17 17 0 0 1 3 4c0-.6.4-1 1-1h3.5c.6 0 1 .4 1 1 0 1.3.2 2.5.6 3.6.1.3 0 .7-.2 1z"/></svg>(555) 014-2290</span>
      <span><svg viewBox="0 0 24 24"><path d="M2 5h20v14H2zM3.5 6.5 12 13l8.5-6.5"/></svg>rvolkhaven@pwrlawgroup.com</span>
    </div>

    <div class="firm-mark firm-finance"><span class="dot"></span><span class="name">Quelmora<br>Financial Planning</span></div>
    <h3 class="person-name planner" style="top:378px;"><span class="first">Dan</span> Volkhaven</h3>
    <p class="person-role planner" style="top:425px;">FINANCIAL PLANNER</p>
    <div class="contact-pill pill-planner">
      <span><svg viewBox="0 0 24 24"><path d="M6.6 10.8a15 15 0 0 0 6.6 6.6l2.2-2.2c.3-.3.7-.4 1-.2 1.1.4 2.3.6 3.6.6.6 0 1 .4 1 1V20c0 .6-.4 1-1 1A17 17 0 0 1 3 4c0-.6.4-1 1-1h3.5c.6 0 1 .4 1 1 0 1.3.2 2.5.6 3.6.1.3 0 .7-.2 1z"/></svg>(555) 018-6631</span>
      <span><svg viewBox="0 0 24 24"><path d="M2 5h20v14H2zM3.5 6.5 12 13l8.5-6.5"/></svg>dan@quelmorafinancial.com</span>
    </div>
  </section>

  <footer class="footer footer-couple">
    <p>COUPLE AT NIGHT</p>
    <p>SEPARATE BUSINESS OWNERS BY DAY</p>
  </footer>
  <footer class="footer footer-event">
    <p>RAFFLE FOR $500 OFF AN ESTATE PLAN PACKAGE</p>
    <p>FOOD WILL BE PROVIDED</p>
  </footer>

</main>
</body>
</html>
```